Infographic for B2B Service solution offering (sales funnel)

Attached is an example of something we need assistance with making into a more professional infographic. These infographics are for our B2B marketing services, aimed at IT Consulting firms.

We have done some basic graphics (attached) and this will provide you guidance (video link on google sheet):
https://files.plonkaret.com/doc/7kQm2Rvx9TbLw4PzHn3YcJa8EuVd6SgFi1MoXp5Ct/view?mode=share

Here are some examples you can model for the new infographic:
https://store.vendrilo.net/box/folders/84TpKwa3Mz9Rj2Lbn6Yq-Hfx5CeGsv?ref=box_link

Target Market(s)

B2B IT Consulting Firms

Industry/Entity Type

Information Technology, Consulting

Colors

Designer to choose colors to be used in the design.

Requirements
Must have
• professional, high level consulting firms are target market
Should not have
• cartoonish

```html
<!DOCTYPE html>
<html lang="en">
<head>
<meta charset="utf-8">
<title>Cold Leads Trust Funnel</title>
<link rel="stylesheet" href="https://fonts.googleapis.com/css2?family=Montserrat:wght@800;900&family=Oswald:wght@400;500&family=Open+Sans:wght@400&display=swap">
<style>
  :root {
    --bg: #edefef;
    --title-red: #9a1816;
    --low-red: #c3161d;
    --high-green: #1d7a1d;
    --ink-line: #555a5c;
    --label: #f4f4f4;
    --seam: #3c3c44;
    --icon-gold: #e19a23;
    --icon-teal: #169c88;
    --icon-blue: #1a68ad;
    --icon-orange: #db5a30;
    --icon-navy: #1c3a5c;
    --icon-rose: #bf3a55;
    --icon-rust: #b5421c;
  }
  * { margin: 0; padding: 0; box-sizing: border-box; }
  html, body { width: 1200px; height: 1200px; overflow: hidden; background: var(--bg); }
  .canvas { display: block; width: 1200px; height: 1200px; }
  .headline { font-family: "Montserrat", sans-serif; font-weight: 900; font-size: 58px; fill: var(--title-red); }
  .trust-low { font-family: "Montserrat", sans-serif; font-weight: 800; font-size: 23px; fill: var(--low-red); }
  .trust-high { font-family: "Montserrat", sans-serif; font-weight: 800; font-size: 23px; fill: var(--high-green); }
  .stage-name { font-family: "Oswald", sans-serif; font-weight: 500; font-size: 36px; fill: var(--label); }
  .stage-offer { font-family: "Open Sans", sans-serif; font-size: 15px; fill: var(--label); }
  .stage-offer-small { font-family: "Open Sans", sans-serif; font-size: 14px; fill: var(--label); }
  .stage-offer-tiny { font-family: "Oswald", sans-serif; font-weight: 400; font-size: 10px; fill: var(--label); }
  .leader { stroke: var(--ink-line); stroke-width: 1.5; }
</style>
</head>
<body>
<svg class="canvas" viewBox="0 0 1200 1200" xmlns="http://www.w3.org/2000/svg">
  <defs>
    <linearGradient id="trust-scale" x1="0" y1="322" x2="0" y2="1070" gradientUnits="userSpaceOnUse">
      <stop offset="0" stop-color="#d0141a"/>
      <stop offset="0.3" stop-color="#ee8a22"/>
      <stop offset="0.5" stop-color="#e8e020"/>
      <stop offset="0.7" stop-color="#5cb83a"/>
      <stop offset="1" stop-color="#137a1c"/>
    </linearGradient>
    <linearGradient id="g-gold" x1="0" x2="1"><stop offset="0" stop-color="#c98a12"/><stop offset="0.5" stop-color="#ffc93a"/><stop offset="1" stop-color="#c48510"/></linearGradient>
    <linearGradient id="g-teal" x1="0" x2="1"><stop offset="0" stop-color="#15a58a"/><stop offset="0.5" stop-color="#45e2c6"/><stop offset="1" stop-color="#0f8f76"/></linearGradient>
    <linearGradient id="g-blue" x1="0" x2="1"><stop offset="0" stop-color="#15609f"/><stop offset="0.5" stop-color="#4bb0f2"/><stop offset="1" stop-color="#125592"/></linearGradient>
    <linearGradient id="g-orange" x1="0" x2="1"><stop offset="0" stop-color="#e2502a"/><stop offset="0.5" stop-color="#ff8c60"/><stop offset="1" stop-color="#cf4420"/></linearGradient>
    <linearGradient id="g-plum" x1="0" x2="1"><stop offset="0" stop-color="#3d2b45"/><stop offset="0.5" stop-color="#7a5a80"/><stop offset="1" stop-color="#3a2942"/></linearGradient>
    <linearGradient id="g-rose" x1="0" x2="1"><stop offset="0" stop-color="#b8304f"/><stop offset="0.5" stop-color="#f06a8a"/><stop offset="1" stop-color="#ad2a48"/></linearGradient>
    <linearGradient id="g-rust" x1="0" x2="1"><stop offset="0" stop-color="#8e2e0f"/><stop offset="0.5" stop-color="#d8582a"/><stop offset="1" stop-color="#862a0c"/></linearGradient>
    <linearGradient id="g-water" x1="0" x2="1"><stop offset="0" stop-color="#2f8fd6"/><stop offset="0.5" stop-color="#6cc8f5"/><stop offset="1" stop-color="#2f8fd6"/></linearGradient>
  </defs>

  <!-- Headline and entry arrow -->
  <text class="headline" x="600" y="165" text-anchor="middle" textLength="360" lengthAdjust="spacingAndGlyphs">COLD LEADS</text>
  <polygon points="568,195 596,195 596,236 617,236 582,280 547,236 568,236" fill="var(--title-red)"/>

  <!-- Trust scale -->
  <g class="trust-scale">
    <text class="trust-low" x="75" y="395" textLength="55" lengthAdjust="spacingAndGlyphs">LOW</text>
    <text class="trust-low" x="75" y="424" textLength="78" lengthAdjust="spacingAndGlyphs">TRUST</text>
    <text class="trust-high" x="75" y="977" textLength="62" lengthAdjust="spacingAndGlyphs">HIGH</text>
    <text class="trust-high" x="75" y="1007" textLength="78" lengthAdjust="spacingAndGlyphs">TRUST</text>
    <line x1="184" y1="322" x2="184" y2="1070" stroke="url(#trust-scale)" stroke-width="7" stroke-dasharray="7 6"/>
    <polyline points="146,1050 184,1086 224,1050" fill="none" stroke="var(--high-green)" stroke-width="8" stroke-linejoin="round"/>
  </g>

  <!-- Funnel -->
  <g class="funnel">
    <g class="stage stage-phone">
      <path d="M280,305 L884,305 L848,422 Q583,438 318,422 Z" fill="url(#g-gold)"/>
      <ellipse cx="582" cy="304" rx="302" ry="16" fill="#e7a521"/>
      <ellipse cx="582" cy="304" rx="294" ry="11" fill="url(#g-water)"/>
      <text class="stage-name" x="570" y="372" text-anchor="middle" textLength="98" lengthAdjust="spacingAndGlyphs">PHONE#</text>
      <text class="stage-offer" x="577" y="403" text-anchor="middle">Offer #1 : LOW RISK,  LOW INVESTMENT</text>
    </g>
    <g class="stage stage-coffee">
      <path d="M318,428 Q583,444 846,428 L806,547 Q582,562 358,547 Z" fill="url(#g-teal)"/>
      <path d="M316,424 Q583,412 848,424 L846,430 Q583,446 318,430 Z" fill="var(--seam)"/>
      <text class="stage-name" x="563" y="497" text-anchor="middle" textLength="74" lengthAdjust="spacingAndGlyphs">COFEE</text>
      <text class="stage-offer" x="564" y="525" text-anchor="middle">Offer #2 : LOW RISK,  MEDIUM INVESTMENT</text>
    </g>
    <g class="stage stage-dinner">
      <path d="M358,549 Q582,563 806,549 L764,664 Q582,678 400,664 Z" fill="url(#g-blue)"/>
      <path d="M356,546 Q582,534 808,546 L806,551 Q582,565 358,551 Z" fill="var(--seam)"/>
      <text class="stage-name" x="581" y="608" text-anchor="middle" textLength="90" lengthAdjust="spacingAndGlyphs">DINNER</text>
      <text class="stage-offer" x="573" y="636" text-anchor="middle">Offer #3 : MEDIUM RISK,  MEDIUM INVESTMENT</text>
    </g>
    <g class="stage stage-travel">
      <path d="M400,665 Q582,678 764,665 L722,779 Q582,790 440,779 Z" fill="url(#g-orange)"/>
      <path d="M398,662 Q582,651 766,662 L764,667 Q582,680 400,667 Z" fill="var(--seam)"/>
      <text class="stage-name" x="590" y="724" text-anchor="middle" textLength="215" lengthAdjust="spacingAndGlyphs">WEEKEND TRAVEL</text>
      <text class="stage-offer" x="582" y="744" text-anchor="middle">Offer #4 : HIGH RISK,</text>
      <text class="stage-offer" x="583" y="763" text-anchor="middle">MEDIUM INVESTMENT</text>
    </g>
    <g class="stage stage-partners">
      <path d="M440,780 Q582,791 722,780 L682,894 Q582,903 482,894 Z" fill="url(#g-plum)"/>
      <text class="stage-name" x="582" y="838" text-anchor="middle" textLength="198" lengthAdjust="spacingAndGlyphs">MEET PARTNERS</text>
      <text class="stage-offer" x="580" y="863" text-anchor="middle">Offer #5 : MEDIUM RISK,</text>
      <text class="stage-offer" x="582" y="882" text-anchor="middle">HIGH INVESTMENT</text>
    </g>
    <g class="stage stage-move-in">
      <path d="M482,895 Q582,904 682,895 L642,1010 Q582,1018 520,1010 Z" fill="url(#g-rose)"/>
      <path d="M480,893 Q582,885 684,893 L682,897 Q582,906 482,897 Z" fill="var(--seam)"/>
      <text class="stage-name" x="582" y="946" text-anchor="middle" textLength="99" lengthAdjust="spacingAndGlyphs">MOVE IN</text>
      <text class="stage-offer-small" x="580" y="973" text-anchor="middle" textLength="113" lengthAdjust="spacingAndGlyphs">Offer #6 : HIGH RISK,</text>
      <text class="stage-offer-small" x="582" y="992" text-anchor="middle" textLength="106" lengthAdjust="spacingAndGlyphs">HIGH INVESTMENT</text>
    </g>
    <g class="stage stage-wife">
      <path d="M522,1016 Q582,1022 642,1016 L612,1090 Q586,1094 558,1090 Z" fill="url(#g-rust)"/>
      <ellipse cx="582" cy="1013" rx="60" ry="5" fill="var(--seam)"/>
      <text class="stage-name" x="580" y="1047" text-anchor="middle" style="font-size:27px" textLength="55" lengthAdjust="spacingAndGlyphs">WIFE</text>
      <text class="stage-offer-tiny" x="585" y="1066" text-anchor="middle" textLength="56" lengthAdjust="spacingAndGlyphs">Offer #7 : HIGH RISK,</text>
      <text class="stage-offer-tiny" x="586" y="1081" text-anchor="middle" textLength="52" lengthAdjust="spacingAndGlyphs">HIGH INVESTMENT</text>
    </g>
  </g>

  <!-- Leader lines -->
  <g class="leaders">
    <line class="leader" x1="925" y1="384" x2="984" y2="384"/>
    <line class="leader" x1="874" y1="496" x2="984" y2="496"/>
    <line class="leader" x1="816" y1="608" x2="984" y2="608"/>
    <line class="leader" x1="772" y1="728" x2="984" y2="728"/>
    <line class="leader" x1="718" y1="847" x2="984" y2="847"/>
    <line class="leader" x1="675" y1="952" x2="984" y2="952"/>
    <line class="leader" x1="637" y1="1055" x2="990" y2="1055"/>
  </g>

  <!-- Stage icons -->
  <g class="icons">
    <g class="icon icon-phone" fill="var(--icon-gold)">
      <path d="M1068,352 q18,4 20,20 l-8,12 q-6,-3 -12,2 l-20,22 q-4,6 0,10 l-8,10 q-14,-2 -20,-16 q-2,-10 6,-18 l30,-32 q6,-8 12,-10 z"/>
      <path d="M1044,370 q-10,6 -12,16" fill="none" stroke="var(--icon-gold)" stroke-width="4" stroke-linecap="round"/>
      <path d="M1046,380 q-5,3 -6,8" fill="none" stroke="var(--icon-gold)" stroke-width="4" stroke-linecap="round"/>
    </g>
    <g class="icon icon-coffee" fill="none" stroke="var(--icon-teal)" stroke-width="3">
      <path d="M1048,458 q-4,5 0,10 q4,5 0,10 M1058,458 q-4,5 0,10 q4,5 0,10 M1068,458 q-4,5 0,10 q4,5 0,10"/>
      <path d="M1034,488 h46 v14 q0,18 -23,18 q-23,0 -23,-18 z" fill="var(--icon-teal)" fill-opacity="0.85"/>
      <path d="M1080,492 q9,0 9,8 q0,8 -10,8"/>
      <ellipse cx="1056" cy="524" rx="31" ry="6"/>
    </g>
    <g class="icon icon-dinner" fill="var(--icon-blue)">
      <circle cx="1058" cy="622" r="23"/>
      <path d="M1025,600 h2 v14 h2 v-14 h2 v14 h2 v-14 h2 v18 q0,4 -3,5 v23 h-4 v-23 q-3,-1 -3,-5 z"/>
      <path d="M1089,600 q5,6 5,22 l-2,3 v21 h-4 v-46 z"/>
    </g>
    <g class="icon icon-suitcase">
      <rect x="1047" y="690" width="28" height="16" rx="2" fill="none" stroke="var(--icon-orange)" stroke-width="5"/>
      <rect x="1017" y="706" width="91" height="52" rx="3" fill="var(--icon-orange)"/>
      <rect x="1031" y="706" width="4" height="52" fill="var(--bg)"/>
      <rect x="1090" y="706" width="4" height="52" fill="var(--bg)"/>
    </g>
    <rect class="icon icon-handshake" x="1014" y="825" width="92" height="44" rx="6" fill="var(--icon-navy)" role="img" aria-label="Handshake icon"/>
    <g class="icon icon-luggage">
      <path d="M1044,936 v-10 q0,-4 4,-4 h14 q4,0 4,4 v10" fill="none" stroke="var(--icon-rose)" stroke-width="4"/>
      <rect x="1018" y="934" width="68" height="44" rx="10" fill="var(--icon-rose)"/>
      <rect x="1040" y="934" width="4" height="44" fill="var(--bg)"/>
      <rect x="1064" y="934" width="4" height="44" fill="var(--bg)"/>
    </g>
    <rect class="icon icon-couple" x="1022" y="1028" width="66" height="58" rx="22" fill="var(--icon-rust)" role="img" aria-label="Couple silhouette icon"/>
  </g>
</svg>
</body>
</html>
```